DL Flyer for vehicle buying/selling service and advice business

New business to help people sell their current vehicle then select and buy and maintain their next car. (New or used).
We'll prepare and sell your car for you and get $,000s more than a trade in.
Offer advice as to the best car currently on the market based on our customer's needs.
With country wide sourcing network of cars across all manufacturers we have great buying power to ensure the very best possible price.
Personal service, including preparation of car for sale, pickup of old and drop-off of new vehicles, organise RWC and any required repairs.
We are NOT a car dealer so we WILL not try to sell you the vehicles we own.
Totally impartial, professional and friendly service making the purchase of your next car a great experience.
Updates

Flyer wording===========“Don’t sell your car or buy your next car without speaking to us”We guarantee to get you a better price for your current car and to find a cheaper purchase price for your next car.With a country wide sourcing network of cars “new and used” across all manufacturers we have sensational buying power to ensure the very best possible price.We can source the right car on any budget, from $2,000 to $200,000We are NOT a car dealer so we WILL not try to sell you the vehicles we own.By not being affiliated with any individual car manufacturer or dealer we can offer absolute impartiality.We’ll sit with you to discuss the best car for your needs and even bring the car to you for a test drive without the pressure of a salesperson nearby.Our services include:• Selling your current car: - Obtaining a roadworthy certificate - Organising any repairs needed - Detailing your car (wash, vacuum, polish) - Advertising of your car - Dealing with potential buyers - Negotiating the best price on your behalf• Assisting with the selection of your next car• Organising test drives• Purchasing the car of your choice - Sourcing the very best price• Ongoing management of their vehicle (service, clean, repair)Possible inclusions in the flyer might be:Advantages of upgrading to a new vehicle include:o reliability, o safety,o fuel efficiencyo comfort.Space for a couple of short testimonials Background images of all of the major car manufacturers Added Friday, July 29, 2016

Target Market(s)

Local community.
Initially will drop DL flyers in local post boxes

Industry/Entity Type

Business

Requirements
Must have
• Flyer wording:
• ===========
• “Don’t sell your car or buy your next car without speaking to us”
• ---------------------------------------------------------------------------------
• We guarantee to get you a better price for your current car and to find a cheaper purchase price for your next car.
• With a country wide sourcing network of cars “new and used” across all manufacturers we have sensational buying power to ensure the very best possible price.
• We can source the right car on any budget, from $2,000 to $200,000
• We are NOT a car dealer so we WILL not try to sell you the vehicles we own.
• By not being affiliated with any individual car manufacturer or dealer we can offer absolute impartiality.
• We’ll sit with you to discuss the best car for your needs and even bring the car to you for a test drive without the pressure of a salesperson nearby.
• Our services include:
• • Selling your current car:
• o Obtaining a roadworthy certificate
• o Organising any repairs needed
• o Detailing your car (wash, vacuum, polish)
• o Advertising of your car
• o Dealing with potential buyers
• o Negotiating the best price on your behalf
• • Assisting with the selection of your next car
• • Organising test drives
• • Purchasing the car of your choice
• o Sourcing the very best price
• • Ongoing management of your vehicle (service, clean, repair)
• Call Gerald on: 0427 315064
Nice to have
• Possible inclusions on the flyer might be:
• List of advantages of upgrading to a new vehicle:
• o reliability,
• o safety,
• o fuel efficiency
• o comfort
• Space for a couple of short testimonials
• Background images of all of the major car manufacturers

```html
<!DOCTYPE html>
<html lang="en">
<head>
<meta charset="utf-8">
<title>Vehicle Brokerage DL Flyer</title>
<link href="https://fonts.googleapis.com/css2?family=Lato:wght@400;700;900&family=Oswald:wght@400;500;600&display=swap" rel="stylesheet">
<style>
  :root{
    --red:#e2202a;
    --red-dark:#c5161f;
    --navy:#1f2a5c;
    --navy-deep:#17204a;
    --ink:#1a1a1a;
    --text:#333640;
    --paper:#ffffff;
    --backdrop:#d9dade;
    --photo-a:#dfe3ea;
    --photo-b:#9aa3b5;
  }
  *{box-sizing:border-box;margin:0;padding:0}
  html,body{width:1200px;height:900px;overflow:hidden}
  body{background:var(--backdrop);font-family:"Lato",Arial,sans-serif;color:var(--text);position:relative}

  .flyer{position:absolute;top:37px;width:413px;height:823px;background:var(--paper);overflow:hidden;box-shadow:0 4px 14px rgba(0,0,0,.25)}
  .flyer--front{left:133px}
  .flyer--back{left:672px}

  .photo{position:absolute;background:linear-gradient(135deg,var(--photo-a),var(--photo-b))}
  .shapes{position:absolute;left:0;top:0;width:413px;height:823px}

  .brand{position:absolute;top:0;left:47px;width:94px;height:120px;background:var(--red);display:flex;flex-direction:column;align-items:center;justify-content:center;color:var(--paper);font-family:"Lato",Arial,sans-serif;font-weight:400;font-size:23px;line-height:1.2;letter-spacing:2px;text-align:center}
  .flyer--back .brand{left:37px}

  .inset-photo{position:absolute;left:262px;top:362px;width:122px;height:140px;background:#6c6a86;transform:rotate(-4deg);padding:8px}
  .inset-photo div{width:100%;height:100%;background:linear-gradient(135deg,#e8e6ea,#8c8a98)}

  .front-copy{position:absolute;left:0;top:512px;width:413px;text-align:center}
  .headline{font-family:"Oswald",Arial,sans-serif;font-weight:500;font-size:29px;line-height:1.1;color:var(--navy)}
  .headline .accent{color:var(--red)}
  .subhead{font-weight:900;font-size:23px;color:var(--ink);margin-top:4px}
  .lede{font-size:15px;line-height:1.35;color:var(--text);margin:8px 18px 0}
  .promise{position:absolute;left:0;top:657px;width:413px;height:46px;background:var(--navy);color:var(--paper);font-weight:700;font-size:15px;line-height:1.2;text-align:center;padding-top:5px}
  .advice{position:absolute;left:0;top:708px;width:413px;text-align:center;font-size:14px;line-height:1.3;color:var(--text);padding:0 30px}

  .call{position:absolute;left:130px;top:755px;color:var(--ink);font-weight:900;font-size:19px;white-space:nowrap}
  .call .num{color:var(--paper);margin-left:6px}
  .web{position:absolute;left:238px;top:783px;color:var(--paper);font-weight:700;font-size:16px}
  .flyer--back .call{left:38px}
  .flyer--back .web{left:42px;top:781px}

  .back-copy{position:absolute;left:0;top:205px;width:413px;text-align:center}
  .claim{font-weight:900;font-size:23px;color:var(--red);line-height:1.1}
  .claim-sub{font-weight:900;font-size:14px;color:var(--navy);line-height:1.3;margin:3px 20px 0}
  .para{font-size:13px;line-height:1.35;color:var(--text);margin:9px 30px 0}

  .label{position:absolute;left:0;height:24px;background:var(--red);color:var(--paper);font-size:13px;line-height:24px;padding-left:40px;letter-spacing:.3px}
  .label--advantages{top:392px;width:157px}
  .label--services{top:626px;width:157px}

  .bullets{position:absolute;list-style:none;font-size:13px;color:var(--text)}
  .bullets li{position:absolute;white-space:nowrap;padding-left:12px}
  .bullets li::before{content:"";position:absolute;left:0;top:6px;width:5px;height:5px;border-radius:50%;background:var(--navy)}

  .budget{position:absolute;left:0;top:472px;width:413px;text-align:center}
  .budget-note{font-size:13px;color:var(--red)}
  .budget-range{font-weight:700;font-size:17px;color:var(--ink);margin-top:3px}

  .testimonials{position:absolute;left:0;top:523px;width:413px;height:100px;background:var(--navy);color:var(--paper)}
  .testimonials h3{position:absolute;left:45px;top:8px;font-weight:400;font-size:13px;border-bottom:1px solid var(--paper)}
  .testimonials p{position:absolute;left:45px;right:30px;top:27px;font-size:10px;line-height:1.4;text-align:center}

  .services{position:absolute;left:40px;top:658px;width:350px;list-style:none;font-size:10.5px;line-height:1.2;color:var(--text)}
  .services li{position:absolute;width:160px;padding-left:10px}
  .services li::before{content:"";position:absolute;left:0;top:4px;width:4px;height:4px;border-radius:50%;background:var(--navy)}
</style>
</head>
<body>

<!-- Front panel -->
<section class="flyer flyer--front">
  <div class="photo" style="left:0;top:80px;width:413px;height:400px" role="img" aria-label="Photo of a family choosing a white car with a salesperson in a showroom"></div>

  <svg class="shapes" viewBox="0 0 413 823" aria-hidden="true">
    <polygon points="0,0 285,0 0,228" fill="var(--red)"/>
    <polygon points="285,0 330,0 0,262 0,228" fill="var(--paper)"/>
    <polygon points="330,0 413,0 413,88 210,118 250,60" fill="var(--navy)"/>
    <polygon points="0,445 260,500 413,470 413,512 0,512" fill="var(--paper)"/>
    <polygon points="0,448 0,492 285,505 240,495" fill="var(--navy)"/>
    <polygon points="0,456 285,505 413,470 413,482 288,512 0,470" fill="var(--red)"/>
    <polygon points="0,750 413,750 413,823 0,823" fill="var(--red)"/>
    <polygon points="0,718 80,823 0,823" fill="var(--navy)"/>
    <polygon points="0,750 55,750 120,823 80,823" fill="var(--paper)"/>
    <polygon points="413,760 413,823 360,823" fill="var(--navy)"/>
  </svg>

  <div class="brand"><span>TBA</span><span>LOGO</span></div>
  <div class="inset-photo" role="img" aria-label="Small photo of a broker reviewing paperwork with customers"><div></div></div>

  <div class="front-copy">
    <h1 class="headline">NEW <span class="accent">(FULL SERVICE)</span></h1>
    <h2 class="subhead">Vehicle Brokerage Business</h2>
    <p class="lede">New business to help people sell their current vehicle then select and buy and maintain their next car. (New or used).</p>
  </div>
  <p class="promise">We'll prepare and sell your car for you and get<br>$,000s more than a trade in.</p>
  <p class="advice">Offer advice as to the best car currently on the market based on our customer's needs.</p>

  <p class="call">CALL US: <span class="num">123 456 7890</span></p>
  <p class="web">www.drivewiseco.com</p>
</section>

<!-- Back panel -->
<section class="flyer flyer--back">
  <div class="photo" style="left:0;top:0;width:413px;height:190px" role="img" aria-label="Photo of a couple and a dealer discussing a car purchase in a showroom"></div>

  <svg class="shapes" viewBox="0 0 413 823" aria-hidden="true">
    <polygon points="0,140 413,185 413,195 0,195" fill="var(--paper)"/>
    <polygon points="0,145 300,178 0,190" fill="var(--navy)"/>
    <polygon points="0,750 413,750 413,823 0,823" fill="var(--red)"/>
    <polygon points="413,735 413,823 330,823" fill="var(--navy)"/>
    <polygon points="330,750 380,750 420,823 370,823" fill="var(--paper)" opacity=".0"/>
  </svg>

  <div class="brand"><span>TBA</span><span>LOGO</span></div>

  <div class="back-copy">
    <h1 class="claim">We are NOT a car dealer</h1>
    <p class="claim-sub">so we WILL not try to sell you the vehicles we own.</p>
    <p class="para">With country wide sourcing network of cars across all manufacturers we have great buying power to ensure the very best possible price.</p>
    <p class="para">Personal service, including preparation of car for sale, pickup of old and drop-off of new vehicles, organise RWC and any required repairs.</p>
  </div>

  <h3 class="label label--advantages">ADVANTAGES:</h3>
  <ul class="bullets" style="left:40px;top:423px">
    <li style="left:0;top:0">Upgrading to a new vehicle,</li>
    <li style="left:180px;top:0">Safety,</li>
    <li style="left:274px;top:-2px">Comfort</li>
    <li style="left:0;top:19px">Including reliability,</li>
    <li style="left:180px;top:19px">Fuel efficiency</li>
  </ul>

  <div class="budget">
    <p class="budget-note">Capability to source new and used cars to any budget</p>
    <p class="budget-range">$2,000 to $200,000</p>
  </div>

  <div class="testimonials">
    <h3>Testimonials:</h3>
    <p>Lorem Ipsum is simply dummy text of the printing and typesetting industry. Lorem Ipsum has been the industry's standard dummy text ever since the 1500s, when an unknown printer took a galley of type and scrambled it to make a type specimen book.</p>
  </div>

  <h3 class="label label--services">OUR SERVICES:</h3>
  <ul class="services">
    <li style="left:0;top:0">Preparation of their current car for sale</li>
    <li style="left:0;top:30px">Obtain RWC and repair any damage</li>
    <li style="left:0;top:62px">Handle the sale of their car</li>
    <li style="left:176px;top:0">Assist with the selection of their next car</li>
    <li style="left:176px;top:30px">Source best price and purchase of their next new/used car</li>
    <li style="left:176px;top:62px">Ongoing management of their vehicle (service, clean, repair)</li>
  </ul>

  <p class="call">CALL US: <span class="num">123 456 7890</span></p>
  <p class="web">www.drivewiseco.com</p>
</section>

</body>
</html>
```